Havenmark Electrical Business Card

create a simple but clear business card and letterhead - needs to be professional not too fancy and direct.

Target Market(s)

Home builders

Contact Information for Business Card

Information needed
Havenmark Electrical Contracting
EC. No. 418237
Derek Hollowell
Mobile 0437215609
derek@havenmarkelectrical.com.au

Requirements
Must have
• logo
• Havenmark Electrical Contracting - H.E.C.
• EC. No. 418237
• Derek Hollowell
• Mobile 0437215609
• derek@havenmarkelectrical.com.au
Nice to have
• black with white printing simple but clear
Should not have
• too much information
• no fancy writing

```html
<!DOCTYPE html>
<html lang="en">
<head>
<meta charset="utf-8">
<title>Havenmark Electrical Contracting – Business Card</title>
<link rel="stylesheet" href="https://fonts.googleapis.com/css2?family=Lato:wght@400;700&family=Arimo:wght@400&display=swap">
<style>
  :root {
    --stage: #5e5e5e;
    --card: #262626;
    --ink: #ffffff;
    --ink-soft: #e6e6e6;
  }
  * { margin: 0; padding: 0; box-sizing: border-box; }
  html, body {
    width: 1200px;
    height: 900px;
    overflow: hidden;
    background: var(--stage);
  }
  .stage {
    position: relative;
    width: 1200px;
    height: 900px;
  }
  .card {
    position: absolute;
    width: 560px;
    height: 320px;
    background: var(--card);
    color: var(--ink);
    box-shadow: 0 10px 30px rgba(0, 0, 0, 0.35);
  }
  .card--back { left: 560px; top: 90px; }
  .card--front { left: 80px; top: 470px; }

  .brand {
    display: flex;
    align-items: center;
    gap: 14px;
  }
  .brand__mark {
    width: 52px;
    height: 52px;
    border-radius: 50%;
    background: var(--ink);
    flex: none;
  }
  .brand__name {
    font-family: "Lato", sans-serif;
    font-weight: 700;
    font-size: 22px;
    line-height: 1.15;
    color: var(--ink);
    width: 230px;
  }

  .card--back .brand {
    position: absolute;
    left: 140px;
    top: 92px;
  }
  .card--back .web {
    position: absolute;
    left: 0;
    right: 0;
    top: 210px;
    text-align: center;
    font-family: "Lato", sans-serif;
    font-size: 15px;
    letter-spacing: 2px;
    color: var(--ink-soft);
  }

  .card--front .brand {
    position: absolute;
    left: 34px;
    top: 30px;
  }
  .holder {
    position: absolute;
    left: 34px;
    top: 132px;
    font-family: "Arimo", sans-serif;
    font-size: 24px;
    color: var(--ink);
  }
  .contact {
    position: absolute;
    left: 250px;
    top: 178px;
    font-family: "Lato", sans-serif;
    font-size: 16px;
    line-height: 24px;
    color: var(--ink-soft);
    list-style: none;
  }
  .contact li {
    display: flex;
    align-items: center;
    gap: 10px;
  }
  .contact .icon {
    width: 14px;
    height: 14px;
    flex: none;
  }
  .contact .plain { padding-left: 0; }
</style>
</head>
<body>
<main class="stage">

  <section class="card card--back" aria-label="Business card, back">
    <div class="brand">
      <span class="brand__mark" aria-hidden="true"></span>
      <span class="brand__name">Havenmark Electrical Contracting</span>
    </div>
    <p class="web">www.havenmarkwire.com</p>
  </section>

  <section class="card card--front" aria-label="Business card, front">
    <div class="brand">
      <span class="brand__mark" aria-hidden="true"></span>
      <span class="brand__name">Havenmark Electrical Contracting</span>
    </div>
    <p class="holder">Derek Hollowell</p>
    <ul class="contact">
      <li class="plain">Havenmark Electrical Contracting</li>
      <li class="plain">EC. No. 418237</li>
      <li>
        <svg class="icon" viewBox="0 0 14 14" aria-hidden="true">
          <rect x="3.5" y="0.8" width="7" height="12.4" rx="1.2" fill="none" stroke="#e6e6e6" stroke-width="1.2"/>
          <rect x="5" y="2.5" width="4" height="6" fill="#e6e6e6"/>
          <circle cx="7" cy="11" r="0.8" fill="#e6e6e6"/>
        </svg>
        <span>0437 215609</span>
      </li>
      <li>
        <svg class="icon" viewBox="0 0 14 14" aria-hidden="true">
          <rect x="0.8" y="2.8" width="12.4" height="8.4" fill="none" stroke="#e6e6e6" stroke-width="1.2"/>
          <polyline points="0.8,2.8 7,8 13.2,2.8" fill="none" stroke="#e6e6e6" stroke-width="1.2"/>
        </svg>
        <span>derek@havenmarkelectrical.com.au</span>
      </li>
    </ul>
  </section>

</main>
</body>
</html>
```